Give Tall Oak Ridge an Online Presence!

Tall Oak Ridge Property Maintenance is an Australian Owned property maintenance company who needs a stand out online presence.

TOR maintains many buildings and sites and wants to appeal to a corporate professional market with their brand new website. TOR is essentially a handyman service offering all maintenance services to home owners, office managers, real estate agents and strata managers.

The Website:
We need a corporate website that appeals to our broader customer base (property owners, property managers, office managers) the copy is being written by a professional so use filler text for now.

Things that we want:
Home page that sets us apart and appeals to the corporate and residential market. The home page needs to not focus on either the residential or commercial market. The home page should focus on our logo and branding. We have a logo already and it is attached to the brief, please use it and try to consider the colour pallette that goes with it. Whilst we want the site to appear strong and manly it is important to remember that 95% of our customers are female so we need the site to be appealing to women. Women need to believe that we are strong, dependable and trustworthy.
We'd like a quote page and potentially also the ability to get a quote from the home page (please don't put it in if it ruins the overall feel of the home page)
An "about us" page
A contact us page
A blog that's built in (we don't want to link to an external blog)
(overall we'd expect to have 6 or 7 pages total)

The site will also need coding - we expect this to be done in a separate project but need you to consider a few things about the coding side of things.

It needs to be iPhone and iPad compatible.

We'd like you to suggest the best CMS that you would use or if you would suggest not using a CMS please let us know with your submissions.

Target Market(s)

Property owners, office managers and property managers who need maintenance on buildings (So all of them)

Industry/Entity Type

Property Maintenance

Requirements
Must have
• Our Logo
Home page
About Us
Residential
Commercial
Real Estate/Strata
Contact Us/Quote
Blog
Nice to have
• Quote form included in home page
Movement on the home page at least
Should not have
• other logos, too much colour
NO FLASH

```html
<!DOCTYPE html>
<html lang="en">
<head>
<meta charset="utf-8">
<title>Tall Oak Ridge Property Maintenance</title>
<link href="https://fonts.googleapis.com/css2?family=Roboto+Condensed:wght@400;700&family=Arimo:wght@400;700&family=Questrial&family=Ubuntu:wght@400;500;700&family=Source+Sans+3:wght@400;600&display=swap" rel="stylesheet">
<style>
:root{
  --topbar:#2f2f31;
  --red:#c8202b;
  --red-dark:#9c1820;
  --orange:#f7941d;
  --orange-light:#fbb040;
  --hero:#2a2628;
  --hero-panel:#363234;
  --navy:#112a4b;
  --yellow:#f5e50f;
  --ink:#333;
  --muted:#666;
  --link:#2a6bb5;
  --strip:#f1f1f1;
  --white:#fff;
}
*{margin:0;padding:0;box-sizing:border-box}
html,body{width:1200px;height:1044px;overflow:hidden}
body{position:relative;background:linear-gradient(90deg,#e4e4e4,#f7f7f7 20%,#f7f7f7 80%,#e4e4e4);font-family:Arimo,Arial,sans-serif;color:var(--ink)}
.abs{position:absolute}
.topbar{left:0;top:0;width:1200px;height:32px;background:var(--topbar)}
.social-top{right:161px;top:4px;display:flex;gap:9px}
.social-top span{width:23px;height:23px;border-radius:4px;background:#8aa7c9}
.header{left:34px;top:32px;width:1048px;height:123px;background:linear-gradient(#fff,#f4f4f4)}
.brand{display:flex;align-items:center;gap:7px;font-family:Ubuntu,sans-serif;font-weight:700;color:var(--orange);line-height:1.05}
.brand .mark{width:16px;height:16px;background:var(--orange);flex:none}
.brand-header{left:150px;top:68px;font-size:17px;width:150px}
.call{left:787px;top:77px;font-family:Arimo,sans-serif;font-weight:700;font-size:18.5px;color:var(--orange)}
.btn{background:linear-gradient(var(--orange-light),var(--orange));color:#fff;font-family:Arimo,sans-serif;font-weight:700;font-size:14.5px;display:flex;align-items:center;justify-content:center;border-radius:3px;box-shadow:0 2px 3px rgba(0,0,0,.25)}
.nav{left:0;top:155px;width:1200px;height:42px;background:linear-gradient(var(--red),var(--red-dark))}
.nav a,.foot-nav a{position:absolute;text-decoration:none;transform:translateX(-50%);white-space:nowrap}
.nav a{top:11px;font-family:"Roboto Condensed",sans-serif;font-weight:700;font-size:17px;color:#fff}
.nav a.current{color:#5a0e12}
.sep{position:absolute;width:1px;background:rgba(255,255,255,.45)}
.hero{left:148px;top:197px;width:904px;height:358px;background:var(--hero)}
.hero-panel{left:148px;top:277px;width:464px;height:160px;background:var(--hero-panel)}
.hero-lead{left:156px;top:280px;font-family:Questrial,sans-serif;font-size:26px;color:#fff}
.hero-title{left:156px;top:312px;font-family:Questrial,sans-serif;font-size:36px;color:var(--orange)}
.hero-body{left:156px;top:364px;width:460px;font-family:Questrial,sans-serif;font-size:18px;line-height:40px;color:#ddd}
.hero-brand{left:612px;top:356px;width:226px;height:50px;justify-content:center;font-size:21px}
.card{font-family:Ubuntu,sans-serif;color:#fff}
.card-name{left:885px;top:382px;font-weight:700;font-size:22px;color:var(--orange)}
.card-pos{left:885px;top:407px;font-weight:500;font-size:18px}
.card-line{left:885px;font-size:17px}
.card-line b{color:var(--orange);margin-right:6px}
.tab{top:522px;height:33px;display:flex;align-items:center;justify-content:center;font-size:20px;color:#fff;background:var(--red)}
.tab.active{background:#fff;color:var(--orange);font-family:"Roboto Condensed",sans-serif}
.band{left:0;top:555px;width:1200px;height:223px;background:#fff}
.news{left:820px;top:513px;width:218px;height:220px;background:var(--navy);border-radius:3px;font-family:"Source Sans 3",sans-serif;padding:12px 10px}
.news h3{font-family:Ubuntu,sans-serif;font-weight:500;font-size:18px;color:var(--yellow);margin-bottom:6px}
.news .date{color:#e8302c;font-size:12px}
.news p{color:#fff;font-size:12.5px;line-height:15px}
.news hr{border:0;border-top:1px dotted #8093b0;margin:10px 0 12px}
.news .all{position:absolute;right:10px;bottom:8px;color:var(--yellow);font-weight:600;font-size:13px}
.photo{left:144px;top:596px;width:176px;height:119px;border:3px solid #c9c9c9;background:linear-gradient(135deg,#6e5a45,#a88f6c 50,#3d342c)}
.intro-title{left:343px;top:595px;font-family:Arimo,sans-serif;font-size:22px;color:var(--orange)}
.intro-body{left:348px;top:624px;width:460px;font-size:13.5px;line-height:24px;color:#444}
.strip{left:135px;top:748px;width:905px;height:138px;background:var(--strip)}
.rule-dark{left:0;top:778px;width:1200px;height:4px;background:#2b2b2b}
.strip-head{font-family:Ubuntu,sans-serif;font-weight:500;font-size:15px;color:#222}
.thin{height:1px;background:#d8d8d8}
.like{left:209px;top:798px;width:36px;height:16px;border:1px solid #a8b6d3;background:#eef1f8;font-size:9px;color:#3b5998;display:flex;align-items:center;justify-content:center}
.fans-count{left:208px;top:826px;font-size:8.5px;color:#333}
.fan{top:840px;width:37px;height:36px;background:linear-gradient(#7b8f6a,#b9b19a)}
.fan-name{top:877px;width:37px;text-align:center;font-size:7px;color:#777}
.rec-avatar{width:36px;height:34px;background:linear-gradient(#c8a48a,#6d5a4e)}
.rec-name{font-size:8px;font-weight:700;color:#3b5998}
.rec-text{font-size:8px;color:#444;line-height:10px;width:180px}
.rec-time{font-size:7.5px;color:#999}
.blog-title{left:788px;top:800px;font-size:11px;color:var(--link)}
.blog-text{left:788px;top:818px;width:215px;font-size:8.5px;line-height:14px;color:#555}
.footer{left:0;top:886px;width:1200px;height:146px;background:linear-gradient(var(--red),#b51d27)}
.footer-base{left:0;top:1032px;width:1200px;height:12px;background:#3a3a3a}
.foot-nav a{top:906px;font-size:14.5px;color:#fff;transform:none}
.foot-nav a.current{color:#6b0f14}
.brand-footer{left:135px;top:960px;width:110px;font-size:14px}
.foot-name{left:292px;top:950px;font-family:Arimo,sans-serif;font-weight:700;font-size:18px;color:var(--orange-light)}
.foot-pos{left:292px;top:975px;font-size:18px;color:#fff}
.foot-line{left:288px;font-size:13px;color:#fff}
.foot-line b{color:var(--orange);font-weight:400}
.stay{left:886px;top:970px;font-size:10.5px;color:var(--yellow)}
.foot-social{top:969px;width:14px;height:14px;background:#7c8fb8}
</style>
</head>
<body>
<div class="abs topbar"></div>
<div class="abs social-top" aria-label="Social links"><span></span><span></span><span></span><span></span></div>

<header class="abs header"></header>
<div class="abs brand brand-header"><span class="mark"></span><span>Tall Oak Ridge Property Maintenance</span></div>
<div class="abs call">Call Us at (097) 521-3380-14</div>
<div class="abs btn" style="left:783px;top:108px;width:123px;height:33px">Free Inspection</div>
<div class="abs btn" style="left:910px;top:108px;width:113px;height:33px">Online Quote</div>

<nav class="abs nav">
  <a class="current" style="left:198px">Home</a>
  <a style="left:309px">Instant Quote</a>
  <a style="left:441px">Free Inspection</a>
  <a style="left:571px">Commercial</a>
  <a style="left:692px">Residential</a>
  <a style="left:821px">Pest Control</a>
  <a style="left:947px">Contact Us</a>
  <span class="sep" style="left:243px;top:13px;height:16px"></span>
  <span class="sep" style="left:372px;top:13px;height:16px"></span>
  <span class="sep" style="left:516px;top:13px;height:16px"></span>
  <span class="sep" style="left:631px;top:13px;height:16px"></span>
  <span class="sep" style="left:751px;top:13px;height:16px"></span>
  <span class="sep" style="left:893px;top:13px;height:16px"></span>
</nav>

<section class="abs hero"></section>
<div class="abs hero-panel"></div>
<div class="abs hero-lead">TOR is essentially a</div>
<div class="abs hero-title">handyman service</div>
<div class="abs hero-body">offering all maintenance services to home owners, office managers, real estate agents and strata managers.</div>
<div class="abs brand hero-brand"><span class="mark"></span><span>Tall Oak Ridge</span></div>
<div class="abs card card-name">Daniel Hart</div>
<div class="abs card card-pos">POSITION</div>
<div class="abs card card-line" style="top:439px"><b>M</b>0412 555 019</div>
<div class="abs card card-line" style="top:462px"><b>E</b>info@torpm.com.au</div>

<div class="abs band"></div>
<div class="abs tab active" style="left:153px;width:113px">About Us</div>
<div class="abs tab" style="left:271px;width:248px">Corporate Services</div>
<div class="abs tab" style="left:524px;width:249px">Residential Services</div>

<aside class="abs news">
  <h3>NEWS &amp; EVENTS</h3>
  <div class="date">October 29, 2012</div>
  <p>Venture Weekly's first-ever list of the 5,000 fastest-growing private Companies in America</p>
  <hr>
  <div class="date">October 29, 2012</div>
  <p>BrightPath Crew completes record breaking 9.0 upgrades</p>
  <div class="all">VIEW ALL &nbsp;»</div>
</aside>

<div class="abs photo" role="img" aria-label="Photo of a tradesman's tool belt and drill"></div>
<div class="abs intro-title">Brief Introduction</div>
<div class="abs intro-body">TOR is essentially a handyman service offering all maintenance services to home owners, office managers, real estate agents and strata managers.</div>
<div class="abs btn" style="left:360px;top:681px;width:157px;height:30px;font-size:15px">LEARN MORE</div>

<div class="abs strip"></div>
<div class="abs rule-dark"></div>
<div class="abs strip-head" style="left:208px;top:759px">Friendpage</div>
<div class="abs thin" style="left:208px;top:788px;width:222px"></div>
<div class="abs like">Like</div>
<div class="abs fans-count">607 people like <b>Bright Home Services</b>.</div>
<div class="abs fan" style="left:208px" role="img" aria-label="Fan profile photo"></div>
<div class="abs fan" style="left:250px" role="img" aria-label="Fan profile photo"></div>
<div class="abs fan" style="left:292px" role="img" aria-label="Fan profile photo"></div>
<div class="abs fan" style="left:334px" role="img" aria-label="Fan profile photo"></div>
<div class="abs fan" style="left:376px" role="img" aria-label="Fan profile photo"></div>
<div class="abs fan-name" style="left:208px">Kim</div>
<div class="abs fan-name" style="left:250px">Jo</div>
<div class="abs fan-name" style="left:292px">Sam</div>
<div class="abs fan-name" style="left:334px">Lee</div>
<div class="abs fan-name" style="left:376px">Ava</div>

<div class="abs strip-head" style="left:492px;top:754px">Friendpage Recommendations</div>
<div class="abs rec-avatar" style="left:493px;top:796px" role="img" aria-label="Reviewer profile photo"></div>
<div class="abs rec-name" style="left:538px;top:795px">Megan Rhodes Tate</div>
<div class="abs rec-text" style="left:540px;top:806px">I have been with this service since purching my home, and also in my office . . . . .</div>
<div class="abs rec-time" style="left:538px;top:829px">last Wednesday</div>
<div class="abs rec-avatar" style="left:493px;top:849px" role="img" aria-label="Reviewer profile photo"></div>
<div class="abs rec-name" style="left:538px;top:848px">Linda Foyle</div>
<div class="abs rec-text" style="left:535px;top:862px">I have been with this service since purching my home, and also in my office . . . . .</div>
<div class="abs rec-time" style="left:538px;top:882px;height:4px;overflow:hidden">last Wednesday</div>

<div class="abs strip-head" style="left:788px;top:758px">From the Blog</div>
<div class="abs thin" style="left:788px;top:787px;width:217px"></div>
<div class="abs blog-title">Lorem ipsum doler sit amet</div>
<div class="abs blog-text">Velit, sed quia non numquam eius modi tempora incidunt ut labore et dolore magnam aliquam minima veniam.</div>
<div class="abs thin" style="left:788px;top:870px;width:217px"></div>

<footer class="abs footer"></footer>
<div class="foot-nav">
  <a class="current" style="left:135px">Home</a>
  <a style="left:220px">Instant Quote</a>
  <a style="left:339px">Free Inspection</a>
  <a style="left:474px">Commercial</a>
  <a style="left:591px">Residential</a>
  <a style="left:711px">Pest Control</a>
  <a style="left:835px">Contact Us</a>
  <span class="sep" style="left:200px;top:906px;height:14px"></span>
  <span class="sep" style="left:323px;top:908px;height:14px"></span>
  <span class="sep" style="left:452px;top:908px;height:14px"></span>
  <span class="sep" style="left:570px;top:908px;height:14px"></span>
  <span class="sep" style="left:690px;top:908px;height:14px"></span>
  <span class="sep" style="left:817px;top:908px;height:14px"></span>
</div>
<div class="abs thin" style="left:135px;top:928px;width:905px;background:rgba(255,255,255,.25)"></div>
<div class="abs brand brand-footer"><span class="mark"></span><span>Tall Oak Ridge</span></div>
<div class="abs foot-name">daniel hart</div>
<div class="abs foot-pos">POSITION</div>
<div class="abs foot-line" style="top:999px"><b>M</b> 0412555019 &nbsp; I &nbsp; Fax (087) 614-5529</div>
<div class="abs foot-line" style="top:1011px"><b>E</b> info@torpm.com.au</div>
<div class="abs stay">Stay Connected</div>
<div class="abs foot-social" style="left:970px"></div>
<div class="abs foot-social" style="left:991px"></div>
<div class="abs foot-social" style="left:1012px"></div>
<div class="abs footer-base"></div>
</body>
</html>
```